Business card for Industrial Automation Company.

The company is called Process and Motion Solutions. We are a systems integration company in South Africa specializing in PLC and SCADA programming, systems integration and industrial automation. Attached find logo and cover letter of the company for a feel of the general look. The website is still under development, so you will have to use your own ideas.

Please blend the colors on the business card as per the logo colors. Must be clean, professional look. Please submit a creative professional design. If a background color is used please do not use dark colored backgrounds.

Target Market(s)

Mining

Industry/Entity Type

Engineering Consultant

Contact Information for Business Card

Fanie du Plessis (NDip Electrical LC; BSc)
Director / Systems Engineer

Postal Address
PO Box 2836
Duinhaven
7395

Physical Address:
Bloubos Street 27
Duinhaven
7395

Tel: +22 548 6172
Cell: +27 82 395 4820
Mail: faniep@pms-za.example
Web: www.pms-za.example

Font styles to use
Sans Serif

Colors

Designer to choose colors to be used in the design.

Requirements
Must have
• Backside of the card must also contain the following:
• Services
• *Industrial Automation
• *Control System design and configuration
• *Systems Integration
• *Equipment Supply
• Industries
• *Mining
• *Factory
• *Oil and Gas
Nice to have
• Colors must blend in with colors of logo. Not too much color and no dark backgrounds.
Should not have
• dark / black background. Preferably white / light background if any.

```html
<!DOCTYPE html>
<html lang="en">
<head>
<meta charset="utf-8">
<title>Process and Motion Solutions – Business Card</title>
<link href="https://fonts.googleapis.com/css2?family=Ubuntu:wght@300;400;500;700&display=swap" rel="stylesheet">
<style>
  :root {
    --navy: #0b3a86;
    --grey: #5a5b5d;
    --paper: #ffffff;
    --backdrop: #eeeae4;
    --text-grey: #4d4e50;
  }
  * { box-sizing: border-box; margin: 0; padding: 0; }
  html, body {
    width: 1200px; height: 800px; overflow: hidden;
    background: var(--backdrop);
    font-family: "Ubuntu", Arial, sans-serif;
  }
  .stage { position: relative; width: 1200px; height: 800px; }
  .card {
    position: absolute; width: 560px; height: 320px;
    background: var(--paper); overflow: hidden;
    box-shadow: 0 6px 18px rgba(0,0,0,0.12);
  }
  .card--back { left: 30px; top: 240px; }
  .card--front { left: 610px; top: 240px; }

  .brand { display: flex; align-items: center; gap: 10px; }
  .brand__mark { width: 34px; height: 34px; border-radius: 50%; background: var(--navy); flex: none; }
  .brand__name { color: var(--navy); font-weight: 700; line-height: 1.02; }
  .tagline { color: var(--text-grey); font-weight: 300; letter-spacing: 0.06em; white-space: nowrap; }

  /* back card */
  .card--back .brand { position: absolute; left: 26px; top: 34px; }
  .card--back .brand__name { font-size: 20px; width: 220px; }
  .card--back .tagline { position: absolute; left: 70px; top: 90px; font-size: 11px; }
  .industries {
    position: absolute; left: 26px; top: 116px;
    color: var(--navy); font-size: 15px; font-weight: 400;
  }
  .services {
    position: absolute; left: 40px; top: 146px; list-style: none;
    color: var(--navy); font-size: 14px; line-height: 1.35;
  }
  .services li::before { content: "*"; }
  .contact {
    position: absolute; left: 350px; top: 26px; width: 200px;
    color: var(--navy); font-size: 10.5px; line-height: 1.35;
  }
  .contact p + p { margin-top: 9px; }
  .name-band {
    position: absolute; left: 0; bottom: 0; width: 380px; height: 62px;
    background: var(--navy); color: #fff; padding: 10px 0 0 26px;
    font-size: 15px; line-height: 1.35;
  }
  .corner-shapes { position: absolute; right: 0; bottom: 0; }

  /* front card */
  .card--front .brand { position: absolute; left: 40px; top: 62px; gap: 14px; }
  .card--front .brand__mark { width: 56px; height: 56px; }
  .card--front .brand__name { font-size: 34px; width: 380px; }
  .card--front .tagline { position: absolute; left: 110px; top: 166px; font-size: 15px; }
  .band-left {
    position: absolute; left: 0; bottom: 40px; width: 130px; height: 30px;
    background: var(--navy);
  }
  .band-right {
    position: absolute; right: 0; bottom: 0; width: 100px; height: 40px;
    background: var(--navy);
  }
  .web-panel {
    position: absolute; left: 110px; bottom: 0; width: 350px; height: 86px;
    background: var(--grey); color: #fff;
    display: flex; align-items: center; justify-content: center;
    font-size: 22px; font-weight: 300; letter-spacing: 0.02em;
  }
</style>
</head>
<body>
<main class="stage">

  <section class="card card--back" aria-label="Card back">
    <div class="brand">
      <span class="brand__mark"></span>
      <span class="brand__name">Process and Motion Solutions</span>
    </div>
    <p class="tagline">Delivering reliable automated control!</p>

    <p class="industries">Services for Mining, Factory, Oil and Gas</p>
    <ul class="services">
      <li>Industrial Automation</li>
      <li>Control System design and configuration</li>
      <li>Systems Integration</li>
      <li>Equipment Supply</li>
    </ul>

    <div class="contact">
      <p>Tel: +22 548 6172<br>Cell: +27 82 395 4820<br>Mail: faniep@pms-za.example<br>Web: www.pms-za.example</p>
      <p>Postal Address<br>PO Box 2836<br>Duinhaven<br>7395</p>
      <p>Physical Address:<br>Bloubos Street 27<br>Duinhaven<br>7395</p>
    </div>

    <div class="name-band">
      Fanie du Plessis (NDip Electrical LC; BSc)<br>
      Director / Systems Engineer
    </div>
    <svg class="corner-shapes" width="180" height="62" viewBox="0 0 180 62" aria-hidden="true">
      <polygon points="0,62 180,20 180,62" fill="var(--navy)"/>
      <polygon points="90,62 180,0 180,40" fill="var(--grey)"/>
    </svg>
  </section>

  <section class="card card--front" aria-label="Card front">
    <div class="brand">
      <span class="brand__mark"></span>
      <span class="brand__name">Process and Motion Solutions</span>
    </div>
    <p class="tagline">Delivering reliable automated control!</p>

    <div class="band-left"></div>
    <div class="band-right"></div>
    <div class="web-panel">www.pms-za.example</div>
  </section>

</main>
</body>
</html>
```